General Contractors need a new Crisp updated Card Design

We need a new business card design for our company of 25 years based in Toronto call Holvaster Building Inc. : Our goal is to be the leading commercial contractors in Toronto by providing exceptional value to our clients. We work very hard to deliver professional, quality, service in conjunction with consistent price competitiveness to all of our clients on every single project.

Target Market(s)

Design & Build Clients

Industry/Entity Type

Construction Company

Contact Information for Business Card

Address:
18 North Tamlin Glen Road, Unit 57, Marbrook Vale, ON, K7T 2R9
Office: 905-218-5937

Holvasters Logo
Employee Job Description
Employee Cell Phone #
Employee Email
www.holvaster-example.com

Colors

Designer to choose colors to be used in the design.

Requirements
Must have
• Quote Company Saying:
• "Professional. Quality. Service."
Nice to have
• New Crisp up to date look. simple & fresh ( Not to Busy)
Should not have
• NO BLUE PRINTS ON THE BUSINESS CARDS

```html
<!DOCTYPE html>
<html lang="en">
<head>
<meta charset="utf-8">
<title>Holvaster Building Inc. – Business Card</title>
<link href="https://fonts.googleapis.com/css2?family=Open+Sans:wght@400;600&family=Tinos:wght@700&display=swap" rel="stylesheet">
<style>
  :root {
    --brand-teal: #00766c;
    --stripe-light: #8cc3bc;
    --ink: #333333;
    --paper: #ffffff;
    --backdrop: #6e6e6e;
    --watermark: #e4efee;
  }
  * { box-sizing: border-box; margin: 0; padding: 0; }
  html, body { width: 1200px; height: 802px; overflow: hidden; }
  body {
    background: var(--backdrop);
    position: relative;
    font-family: "Open Sans", Arial, sans-serif;
  }
  .card {
    position: absolute;
    top: 274px;
    width: 442px;
    height: 265px;
    box-shadow: 2px 3px 6px rgba(0,0,0,0.45);
    overflow: hidden;
  }
  /* Contact side */
  .card--contact { left: 136px; background: var(--paper); }
  .contact-band {
    position: absolute; left: 0; top: 0; bottom: 0; width: 75px;
    background: var(--brand-teal);
  }
  .contact-band-edge {
    position: absolute; left: 75px; top: 0; bottom: 0; width: 5px;
    background: var(--stripe-light);
  }
  .contact-accent {
    position: absolute; left: 316px; top: 40px; width: 126px; height: 190px;
    background: var(--watermark); opacity: 0.7;
  }
  .contact-details {
    position: absolute; left: 112px; top: 59px;
    color: var(--ink); font-size: 12.8px; line-height: 15.8px;
  }
  .person-name {
    font-family: "Tinos", "Times New Roman", serif;
    font-weight: 700; font-size: 16px; line-height: 18px;
    color: var(--brand-teal); letter-spacing: 0.2px;
  }
  .person-role { margin-bottom: 5px; }
  .contact-line { display: flex; align-items: center; gap: 6px; }
  .contact-line svg { width: 9px; height: 9px; flex: none; fill: var(--brand-teal); }
  .address { margin-top: 6px; }
  /* Brand side */
  .card--brand { left: 624px; background: var(--brand-teal); color: var(--paper); }
  .brand-lockup {
    position: absolute; left: 86px; top: 90px;
    display: flex; align-items: center; gap: 12px;
  }
  .brand-square { width: 58px; height: 58px; background: var(--paper); flex: none; }
  .brand-name {
    font-family: "Tinos", "Times New Roman", serif; font-weight: 700;
    font-size: 28px; line-height: 28px; letter-spacing: 0.5px;
  }
  .brand-name span { display: block; }
  .brand-name .brand-sub { font-size: 17.5px; line-height: 24px; letter-spacing: 2px; }
  .tagline {
    position: absolute; left: 0; right: 0; top: 175px; text-align: center;
    font-weight: 600; font-size: 13px; letter-spacing: 0.2px;
  }
</style>
</head>
<body>
  <section class="card card--contact">
    <div class="contact-band"></div>
    <div class="contact-band-edge"></div>
    <div class="contact-accent"></div>
    <div class="contact-details">
      <p class="person-name">DANIEL MERCER</p>
      <p class="person-role">Managing Director</p>
      <p class="contact-line">
        <svg viewBox="0 0 10 10"><path d="M1 3 Q5 0 9 3 L8 4.5 L6.5 3.8 L6.5 3 Q5 2.6 3.5 3 L3.5 3.8 L2 4.5 Z M2.5 5 H7.5 L8.5 9 H1.5 Z"/></svg>905-218-5937</p>
      <p class="contact-line">
        <svg viewBox="0 0 10 10"><path d="M3 0.5 H7 V9.5 H3 Z M3.8 1.5 V7.5 H6.2 V1.5 Z"/></svg>044-376 812 504</p>
      <p class="contact-line">
        <svg viewBox="0 0 10 10"><path d="M0.5 2 H9.5 V8 H0.5 Z M1.2 2.7 L5 5.5 L8.8 2.7 Z" fill-rule="evenodd"/></svg>info@holvaster-mail.com</p>
      <p class="contact-line">
        <svg viewBox="0 0 10 10"><circle cx="5" cy="5" r="4.5"/></svg>www.holvaster-example.com</p>
      <p class="address">18 North Tamlin Glen Road<br>Unit 57, Marbrook Vale<br>ON, K7T 2R9</p>
    </div>
  </section>

  <section class="card card--brand">
    <div class="brand-lockup">
      <div class="brand-square"></div>
      <p class="brand-name"><span>HOLVASTER</span><span class="brand-sub">BUILDING INC.</span></p>
    </div>
    <p class="tagline">PROFESSIONAL. QUALITY. SERVICE</p>
  </section>
</body>
</html>
```